Investor Information Presentation Design Required and Corporate overview design

I have all the materials ready to go, just need 1x Pro Design for the presentation and 1x Pro Design for the corporate overview.
I am ok with images being changed (only if it represents the company better). Wording Can NOT be changed. Any process diagrams can be changed to better represent the process.
I can provide high res Logo file and obviously the files for the presentation and corporate overview. What I have done is basic, but need it to look far more polished and professional.

Target Market(s)

Fixed Term Deposits - $100,000 + High interest rates

Industry/Entity Type

Investment

Font styles to use
Sans Serif

Requirements
Must have
• A corporate professional look, think banks, financial services, business etc
• The presentation is NOT used for group presenting purposes - Individuals go through it on their own. Should want to make me feel like I have to read it all!

```html
<!DOCTYPE html>
<html lang="en">
<head>
<meta charset="utf-8">
<title>Northvale Capital – High Yield Term Deposits</title>
<link rel="stylesheet" href="https://fonts.googleapis.com/css2?family=Questrial&family=Carlito&display=swap">
<style>
  :root{
    --canvas:#ffffff;
    --cover-grey:#b1b2b4;
    --cover-band:#9d9ea1;
    --navy:#1d2a4a;
    --slate:#5a5b5f;
    --slate-dark:#46474a;
    --paper:#ffffff;
    --paper-soft:#f3f3f4;
    --ink:#2e2f33;
    --ink-soft:#4a4b50;
    --accent:#1fa3dd;
    --rule:#3a3b40;
    --badge:#8d8e92;
  }
  *{box-sizing:border-box;margin:0;padding:0}
  html,body{width:1200px;height:1160px;overflow:hidden;background:var(--canvas)}
  body{position:relative;font-family:"Questrial",sans-serif;color:var(--ink)}

  .slide{position:absolute;width:500px;height:316px;overflow:hidden;box-shadow:0 3px 7px rgba(0,0,0,.35)}
  .slide--cover{left:62px;top:62px;background:var(--cover-grey)}
  .slide--contents{left:641px;top:58px;background:var(--paper)}
  .slide--problem{left:62px;top:420px;background:var(--slate)}
  .slide--solution{left:641px;top:407px;background:var(--paper-soft)}
  .slide--rates{left:64px;top:785px;background:var(--paper)}
  .slide--notes{left:641px;top:782px;background:var(--paper)}

  /* cover */
  .cover-name{position:absolute;left:0;right:0;top:175px;text-align:center;font-size:17px;letter-spacing:.5px;color:var(--navy)}
  .cover-rule{position:absolute;left:155px;width:190px;top:198px;height:1px;background:rgba(255,255,255,.7)}
  .cover-tagline{position:absolute;left:0;right:0;top:201px;text-align:center;font-size:16px;color:#fff}
  .cover-footer{position:absolute;left:0;right:0;top:294px;height:11px;background:var(--cover-band);display:flex;justify-content:space-between;align-items:center;padding:0 56px 0 56px;font-size:3.6px;color:#2b2c30}

  /* shared slide chrome */
  .slide-title{position:absolute;left:48px;top:28px;font-size:22px;color:var(--ink);white-space:nowrap}
  .slide--problem .slide-title{color:#fff}
  .title-rule{position:absolute;left:48px;width:404px;top:59px;height:1px;background:var(--rule)}
  .slide--problem .title-rule{background:#2f3033}
  .title-rule::before{content:"";position:absolute;left:0;top:-1px;width:16px;height:3px;background:var(--accent)}
  .title-rule::after{content:"";position:absolute;left:72px;top:-1px;width:20px;height:2px;background:#3f4f8a}
  .page-marker{position:absolute;left:48px;bottom:8px;height:16px;border-left:1px solid rgba(0,0,0,.2);padding-left:5px;display:flex;align-items:center}
  .slide--problem .page-marker{border-left-color:rgba(255,255,255,.15)}
  .page-badge{font-size:6.5px;color:#fff;background:var(--badge);border-radius:2px;padding:1px 4px}

  .bullets{list-style:none}
  .bullets li{position:relative;padding-left:12px}
  .bullets li::before{content:"";position:absolute;left:0;top:.55em;width:4px;height:4px;border-radius:50%;background:var(--accent);box-shadow:0 0 0 1.5px rgba(31,163,221,.25)}

  /* contents */
  .photo{position:absolute}
  .contents-photo{left:243px;top:0;right:0;bottom:0;background:linear-gradient(160deg,#f3f1ee 0%,#e5e0d6 35%,#c9a24a 62%,#9c7a2c 78%,#d8d2c6 100%)}
  .contents-list{position:absolute;left:50px;top:88px;font-size:9.5px;line-height:20px;color:var(--ink-soft)}

  /* problem */
  .problem-card{position:absolute;top:108px;width:128px;height:111px;background:var(--slate-dark);display:flex;align-items:center;justify-content:center}
  .problem-card svg{width:70px;height:70px}
  .problem-caption{position:absolute;top:227px;width:128px;text-align:center;font-size:7px;line-height:13.5px;color:#d5d6d8}
  .problem-caption .dot{display:inline-block;width:4px;height:4px;border-radius:50%;background:var(--accent);margin-right:5px;vertical-align:1px}

  /* solution */
  .solution-photo{left:279px;top:59px;right:0;bottom:0;background:linear-gradient(180deg,#e9e4e6 0%,#d8cfcf 45%,#b5ada2 75%,#cfc8be 100%)}
  .solution-intro{position:absolute;left:52px;top:98px;width:215px;font-size:9px;line-height:20px;color:var(--ink-soft)}
  .solution-list{position:absolute;left:52px;top:178px;width:215px;font-size:9px;line-height:20px;color:var(--ink-soft)}
  .solution-list li{padding-left:18px}

  /* rates & notes backdrop */
  .backdrop{position:absolute;left:0;right:0;top:59px;bottom:0;background:
    radial-gradient(ellipse 80px 26px at 70px 200px,rgba(120,110,105,.45),transparent),
    radial-gradient(ellipse 90px 24px at 250px 205px,rgba(130,130,140,.35),transparent),
    radial-gradient(ellipse 90px 26px at 410px 195px,rgba(120,125,140,.35),transparent),
    linear-gradient(100deg,#e9e2d8 0%,#ece9e6 45%,#d7dde5 80%,#c7d0dc 100%)}
  .rates-panel{position:absolute;left:66px;top:86px;width:382px;height:142px;background:rgba(120,121,126,.72)}
  .rates-table{position:absolute;left:22px;top:23px;width:339px;border-collapse:collapse;font-family:"Carlito",sans-serif;font-size:9px;color:#fff;text-align:center}
  .rates-table th,.rates-table td{border:1px solid rgba(255,255,255,.85);font-weight:400}
  .rates-table th{height:31px;line-height:11px;vertical-align:top;padding-top:3px}
  .rates-table td{height:17.6px}

  .notes-heading{position:absolute;left:72px;top:86px;font-size:8.5px;text-decoration:underline;color:var(--ink)}
  .notes-list{position:absolute;left:58px;top:107px;width:420px;font-size:6.4px;line-height:20px;color:var(--ink)}
  .notes-list li{padding-left:14px}
</style>
</head>
<body>

<section class="slide slide--cover">
  <div class="cover-name">Northvale Capital</div>
  <div class="cover-rule"></div>
  <div class="cover-tagline">High Yield Term Deposits</div>
  <footer class="cover-footer">
    <span>Northvale Capital Pty Ltd ACN: 512 604 318</span>
    <span>Head Office: Level 9, Harbourline House, 27 Quayside Rd, Southbank 3006 VIC</span>
  </footer>
</section>

<section class="slide slide--contents">
  <div class="photo contents-photo" role="img" aria-label="Photo of stacked gold coins beside a laptop with a pie chart"></div>
  <h2 class="slide-title">Content</h2>
  <div class="title-rule"></div>
  <ul class="bullets contents-list">
    <li>The Problem</li>
    <li>The Solution</li>
    <li>Attractive Term Deposits</li>
    <li>Who is Northvale Capital?</li>
    <li>Happy Investors Globally</li>
    <li>Experienced Senior Management</li>
    <li>Get Started</li>
  </ul>
  <div class="page-marker"><span class="page-badge">01</span></div>
</section>

<section class="slide slide--problem">
  <h2 class="slide-title">The Problem</h2>
  <div class="title-rule"></div>

  <div class="problem-card" style="left:48px">
    <svg viewBox="0 0 70 70" fill="none" stroke="#1fa3dd" stroke-width="2.2">
      <circle cx="35" cy="35" r="33"/>
      <rect x="18" y="25" width="32" height="18" rx="1.5" fill="#1fa3dd" stroke="none"/>
      <rect x="21" y="28" width="26" height="12" fill="#46474a" stroke="none"/>
      <circle cx="34" cy="34" r="4.5" fill="#1fa3dd" stroke="none"/>
      <path d="M20 46h30M53 29v14" stroke-width="2.4"/>
    </svg>
  </div>
  <div class="problem-card" style="left:186px">
    <svg viewBox="0 0 70 70" fill="none" stroke="#1fa3dd" stroke-width="2.2">
      <circle cx="35" cy="35" r="33"/>
      <circle cx="42" cy="29" r="11" stroke-width="2.6"/>
      <path d="M42 22v7l5 3"/>
      <circle cx="28" cy="41" r="11" fill="#1fa3dd" stroke="#46474a" stroke-width="2"/>
      <text x="28" y="46" text-anchor="middle" font-family="Questrial, sans-serif" font-size="14" fill="#46474a" stroke="none">$</text>
    </svg>
  </div>
  <div class="problem-card" style="left:323px">
    <svg viewBox="0 0 70 70" fill="none" stroke="#1fa3dd" stroke-width="2.2">
      <circle cx="35" cy="35" r="33"/>
      <rect x="19" y="38" width="8" height="12" fill="#1fa3dd" stroke="none"/>
      <rect x="30" y="33" width="8" height="17" fill="#1fa3dd" stroke="none"/>
      <rect x="41" y="28" width="8" height="22" fill="#1fa3dd" stroke="none"/>
      <path d="M19 34l9-8 6 5 13-11" stroke-width="2.6"/>
      <path d="M42 19h6v6" stroke-width="2.6"/>
    </svg>
  </div>

  <p class="problem-caption" style="left:48px"><span class="dot"></span>Term deposits with leading banks<br>pay less than 4.0% per annum</p>
  <p class="problem-caption" style="left:186px"><span class="dot"></span>Savings are getting eroded<br>by inflation</p>
  <p class="problem-caption" style="left:323px"><span class="dot"></span>Banks continue to profit despite<br>paying low rates of return</p>

  <div class="page-marker"><span class="page-badge">02</span></div>
</section>

<section class="slide slide--solution">
  <div class="photo solution-photo" role="img" aria-label="Photo of rising coin stacks with a small tree growing from the tallest stack"></div>
  <h2 class="slide-title">The Solution</h2>
  <div class="title-rule"></div>
  <p class="solution-intro">Place your money with Northvale Capital to benefit from -</p>
  <ul class="bullets solution-list">
    <li>A fixed, high rate of return</li>
    <li>Quarterly interest payments</li>
    <li>Keeping ahead of inflation</li>
    <li>Access to other lucrative investment opportunities</li>
  </ul>
  <div class="page-marker"><span class="page-badge">03</span></div>
</section>

<section class="slide slide--rates">
  <div class="backdrop" role="img" aria-label="Soft blurred photo of an office meeting in warm and blue tones"></div>
  <h2 class="slide-title">Attractive Term Deposits</h2>
  <div class="title-rule"></div>
  <div class="rates-panel">
    <table class="rates-table">
      <colgroup><col style="width:99px"><col style="width:124px"><col style="width:116px"></colgroup>
      <tr><th>Term</th><th>Investment Size</th><th>Effective Annual Interest rate</th></tr>
      <tr><td>3 months</td><td>$100k-$5m</td><td>5.95%</td></tr>
      <tr><td>6 months</td><td>$100k-$5m</td><td>6.40%</td></tr>
      <tr><td>12 months</td><td>$100k-$5m</td><td>6.95%</td></tr>
      <tr><td>24 months</td><td>$100k-$5m</td><td>7.40%</td></tr>
    </table>
  </div>
  <div class="page-marker"><span class="page-badge">04</span></div>
</section>

<section class="slide slide--notes">
  <div class="backdrop" role="img" aria-label="Soft blurred photo of an office meeting in warm and blue tones"></div>
  <h2 class="slide-title">Attractive Term Deposits</h2>
  <div class="title-rule"></div>
  <p class="notes-heading">Note:</p>
  <ul class="bullets notes-list">
    <li>Interest begins accruing from the day the funds arrive in the Northvale Capital bank account</li>
    <li>Each deposit is structured as a loan to Northvale Capital Pty Ltd per the terms of the Deposit Agreement</li>
    <li>Northvale Capital automatically deposits the interest in your account each calendar quarter on 1 January, 1 April, 1 July and 1 October</li>
    <li>Deposit Agreements automatically roll over for a further term unless the depositor provides no less than</li>
    <li>14 days notice prior to the end of the deposit term should they wish to withdraw part or all of their principal</li>
  </ul>
  <div class="page-marker"><span class="page-badge">05</span></div>
</section>

</body>
</html>
```